New Business Card Design for Manufacturing

We are an engineering/manufacturing company that offers Advanced machining/assembly/engineering services, as well as innovative products for the heavy duty engine cooling markets.

We are looking to get a new business card designed that is clean and modern looking, but still fits the wide range of technical/skilled work we do.

- We hope to use this design as the base for other design work in new Presentations, web, and print work.

Industry/Entity Type

Engineering

Contact Information for Business Card

Our preferred color of blue is (RGB) 22/71/159 but can vary slightly from that color. Our content will be our Logo and full company name (Fabricated Tooling Works, Inc.), company address, name, job title, phone number with extension, cell number, fax number, website, and email address on the cards.
We'd like the full company name next to the logo, but we are open to other interpretations of that layout.
Preferably, we would like the back side to be clean with just our logo, and the front to contain all of the contact information.

Colors
2f74b4
0355a3
85abd2

Requirements
Must have
• - Logo, company name, needed content - We are open to interpretation beyond that.
• - Standard size business card.
• - Horizontal orientation.
• - Enough space for lengthy names / job titles (for example, a job title could read "Directory of Human Resources" or "V.P. of Governmental Affairs"). We need this to look clean, whether the title be short (CEO) or long (as described above).

```html
<!DOCTYPE html>
<html lang="en">
<head>
<meta charset="utf-8">
<title>Fabricated Tooling Works, Inc. – Business Card</title>
<link href="https://fonts.googleapis.com/css2?family=Arimo:wght@400;700&display=swap" rel="stylesheet">
<style>
  :root {
    --brand-blue: #16479f;
    --paper: #ffffff;
    --backdrop: #eceef1;
    --ink-light: #ffffff;
    --card-shadow: rgba(20, 30, 50, 0.18);
  }
  * { box-sizing: border-box; margin: 0; padding: 0; }
  html, body {
    width: 1200px;
    height: 930px;
    overflow: hidden;
    background: var(--backdrop);
    font-family: "Arimo", Arial, sans-serif;
  }
  .canvas {
    position: relative;
    width: 1200px;
    height: 930px;
  }
  .card {
    position: absolute;
    left: 320px;
    width: 560px;
    height: 320px;
    background: var(--paper);
    box-shadow: 0 10px 28px var(--card-shadow);
    overflow: hidden;
  }
  .card--front { top: 115px; display: flex; }
  .card--back { top: 495px; }

  /* Front: contact panel */
  .contact-panel {
    width: 300px;
    height: 100%;
    background: var(--brand-blue);
    color: var(--ink-light);
    padding: 40px 28px 0 34px;
  }
  .contact-name {
    font-weight: 700;
    font-size: 20px;
    letter-spacing: 0.5px;
    text-transform: uppercase;
  }
  .contact-title {
    font-size: 8.5px;
    letter-spacing: 0.6px;
    text-transform: uppercase;
    margin-top: 4px;
  }
  .contact-address {
    font-size: 13px;
    line-height: 1.45;
    margin-top: 24px;
  }
  .contact-lines {
    list-style: none;
    margin-top: 18px;
    font-size: 12px;
    line-height: 1.55;
  }
  .contact-lines li { display: flex; align-items: center; gap: 8px; }
  .contact-lines svg { width: 10px; height: 10px; flex: none; }

  /* Front: identity side */
  .identity-panel {
    flex: 1;
    display: flex;
    flex-direction: column;
    justify-content: center;
    padding-left: 34px;
    color: var(--brand-blue);
  }
  .brand-row { display: flex; align-items: center; gap: 10px; }
  .brand-square {
    width: 22px; height: 22px;
    background: var(--brand-blue);
    flex: none;
  }
  .brand-name {
    font-weight: 700;
    font-size: 46px;
    letter-spacing: 1px;
    line-height: 1;
  }
  .brand-tagline {
    font-weight: 700;
    font-size: 12px;
    letter-spacing: 1px;
    text-transform: uppercase;
    margin-top: 8px;
  }

  /* Back */
  .back-lockup {
    position: absolute;
    left: 110px;
    top: 108px;
    display: flex;
    align-items: flex-start;
    gap: 22px;
    color: var(--brand-blue);
  }
  .back-lockup .brand-name { font-size: 58px; }
  .company-name {
    font-weight: 700;
    font-size: 15px;
    letter-spacing: 1px;
    line-height: 1.2;
    text-transform: uppercase;
    padding-top: 6px;
    border-left: 2px solid var(--brand-blue);
    padding-left: 14px;
  }
  .company-name small { font-size: 9px; }
</style>
</head>
<body>
<main class="canvas">

  <section class="card card--front" aria-label="Business card front">
    <div class="contact-panel">
      <h1 class="contact-name">Daniel Hart</h1>
      <p class="contact-title">Directory of Human Resources</p>
      <p class="contact-address">P.O. Box 4821, Marlow Street,<br>Leeds, United Kingdom</p>
      <ul class="contact-lines">
        <li>
          <svg viewBox="0 0 10 10" aria-hidden="true"><path fill="currentColor" d="M2 0.5 L3.8 2.8 L2.8 3.8 Q4 6 6.2 7.2 L7.2 6.2 L9.5 8 L8.3 9.5 Q1.5 8 0.5 1.7 Z"/></svg>
          Tel: 0044 2079461032
        </li>
        <li>
          <svg viewBox="0 0 10 10" aria-hidden="true"><rect x="2.5" y="0.5" width="5" height="3" fill="currentColor"/><rect x="0.5" y="3.5" width="9" height="4" fill="currentColor"/><rect x="2.5" y="6.5" width="5" height="3" fill="none" stroke="currentColor"/></svg>
          Fax: 0044 2079461033
        </li>
        <li>
          <svg viewBox="0 0 10 10" aria-hidden="true"><rect x="0.5" y="2" width="9" height="6.5" fill="none" stroke="currentColor"/><path d="M0.5 2 L5 6 L9.5 2" fill="none" stroke="currentColor"/></svg>
          Email: info@ftworks.com
        </li>
        <li>
          <svg viewBox="0 0 10 10" aria-hidden="true"><circle cx="5" cy="5" r="4.4" fill="none" stroke="currentColor"/><ellipse cx="5" cy="5" rx="2" ry="4.4" fill="none" stroke="currentColor"/><path d="M0.6 5 H9.4" stroke="currentColor"/></svg>
          Web: www.ftworks.com
        </li>
      </ul>
    </div>
    <div class="identity-panel">
      <div class="brand-row">
        <span class="brand-square" aria-hidden="true"></span>
        <span class="brand-name">FTW</span>
      </div>
      <p class="brand-tagline">Built to Perform</p>
    </div>
  </section>

  <section class="card card--back" aria-label="Business card back">
    <div class="back-lockup">
      <div>
        <div class="brand-row">
          <span class="brand-square" aria-hidden="true"></span>
          <span class="brand-name">FTW</span>
        </div>
        <p class="brand-tagline">Built to Perform</p>
      </div>
      <p class="company-name">Fabricated<br>Tooling<br>Works <small>Inc</small></p>
    </div>
  </section>

</main>
</body>
</html>
```